School Shop icons

Progressive and fun school needs some 8 icons to appear on our school on line shop. Check school web site www.brambleridge.school.nz for feel. Nice to have a common feel, character or sense of theme.

Essentially I need an icon to locate on the front page of our web site to hyper link to our school shop ( refer current example 1). Thereafter I need 7 icons to appear at the shop front (refer example 2). The 6 icons are (refer example 3) (1.) School Donations (where parents pay their school fee / donation), (2.) Trips and Activities (class trips and activities like sports days), (3.) Uniform (school uniform sales) (4.) Food day (where parents order lunch) (5.) Events (like a parents fund raising event, show, guest speaker) (6.) School camps (we do heaps of outdoor stuff) and (7.)Tuition (not shown - music lessons, dance, second language etc).

I see our school as creative and "little out of the box" and colourful.

In summary 7 icons - need to be simple and clear - I just don't like clip art.

attached guidelines and examples, also screen shot of current branding and colours used in our on line newsletter ( might not help).

Target Market(s)

The parents of my school

Industry/Entity Type

School

Requirements
Must have
• Consistency across the icons
Nice to have
• sense of fun and different
Should not have
• Clip art feel

```html
<!DOCTYPE html>
<html lang="en">
<head>
<meta charset="utf-8">
<title>Bramble Ridge School – Shop Icons</title>
<link rel="stylesheet" href="https://fonts.googleapis.com/css2?family=Arimo:wght@700&family=Open+Sans:wght@400&display=swap">
<style>
  :root {
    --bg: #ffffff;
    --navy: #2a2a45;
    --donation: #f0ab00;
    --trips: #c63b22;
    --uniform: #3aafe2;
    --food: #a967bb;
    --events: #fc5a1c;
    --camps: #3e5ce0;
    --tuition: #72b94a;
    --ink: #111111;
    --link: #777777;
    --white: #ffffff;
  }
  html, body {
    margin: 0;
    padding: 0;
    overflow: hidden;
    background: var(--bg);
  }
  .canvas {
    position: relative;
    width: 1200px;
    height: 900px;
    overflow: hidden;
    background: var(--bg);
  }
  .shop-badge {
    position: absolute;
    left: 196px;
    top: 216px;
    width: 184px;
    height: 184px;
  }
  .category-icon {
    position: absolute;
    left: 659px;
    width: 60px;
    height: 60px;
  }
  .category-label {
    position: absolute;
    left: 784px;
    font-family: "Arimo", Arial, sans-serif;
    font-weight: 700;
    font-size: 10.5px;
    line-height: 13px;
    color: var(--ink);
  }
  .category-label .shop-link {
    display: block;
    margin-left: 4px;
    font-size: 12px;
    line-height: 13px;
    color: var(--link);
    text-decoration: underline;
  }
  .tuition-label {
    position: absolute;
    left: 781px;
    top: 672px;
    font-family: "Open Sans", Arial, sans-serif;
    font-size: 12px;
    color: var(--ink);
  }
</style>
</head>
<body>
<main class="canvas">

  <svg class="shop-badge" viewBox="-92 -92 184 184" aria-label="School shop">
    <circle r="92" fill="var(--navy)"/>
    <g fill="var(--white)">
      <rect x="-38" y="-50" width="76" height="6" rx="3"/>
      <path d="M-37 -41 H37 L50 -20 H-50 Z"/>
      <path d="M-50 -20 H50 V-14 A6 6 0 0 1 38 -14 A12.5 12 0 0 1 13 -14 A12.5 12 0 0 1 -12 -14 A12.5 12 0 0 1 -37 -14 A6.5 6 0 0 1 -50 -14 Z"/>
      <rect x="-42" y="-12" width="6" height="56"/>
      <rect x="36" y="-12" width="6" height="56"/>
      <rect x="-18" y="-8" width="5" height="52"/>
      <rect x="-52" y="43" width="104" height="6" rx="3"/>
      <rect x="-28" y="10" width="4" height="18" rx="2"/>
    </g>
    <g stroke="var(--navy)" stroke-width="3" stroke-linecap="round">
      <line x1="-28" y1="-37" x2="-33" y2="-26"/>
      <line x1="-16" y1="-37" x2="-19" y2="-26"/>
      <line x1="0" y1="-37" x2="0" y2="-26"/>
      <line x1="16" y1="-37" x2="19" y2="-26"/>
      <line x1="28" y1="-37" x2="33" y2="-26"/>
    </g>
    <g stroke="var(--white)" stroke-width="3" stroke-linecap="round">
      <line x1="6" y1="14" x2="17" y2="3"/>
      <line x1="10" y1="20" x2="22" y2="8"/>
    </g>
  </svg>

  <svg class="category-icon" style="top:202px" viewBox="-30 -30 60 60" aria-label="School donation">
    <circle r="30" fill="var(--donation)"/>
    <circle cx="-2" cy="-12" r="7" fill="var(--white)"/>
    <text x="-2" y="-8.5" font-size="10" font-family="Arimo, sans-serif" font-weight="700" text-anchor="middle" fill="var(--donation)">$</text>
    <path d="M-15 4 A14 10 0 0 1 12 -1 L17 -1 L17 6 L13 8 L12 13 L7 13 L7 10 L-7 10 L-7 13 L-12 13 L-12 9 A10 8 0 0 1 -15 4 Z" fill="var(--white)"/>
  </svg>

  <svg class="category-icon" style="top:279px" viewBox="-30 -30 60 60" aria-label="Trips and activities">
    <circle r="30" fill="var(--trips)"/>
    <path d="M-16 -4 A18 15 0 0 1 20 -4 Z" fill="var(--white)"/>
    <rect x="1" y="-4" width="3" height="24" fill="var(--white)"/>
    <rect x="1.5" y="-23" width="2" height="4" fill="var(--white)"/>
    <circle cx="-11" cy="9" r="9" fill="var(--white)"/>
    <path d="M-18 6 Q-11 10 -4 4 M-13 2 Q-9 10 -12 17" stroke="var(--trips)" stroke-width="2" fill="none"/>
  </svg>

  <svg class="category-icon" style="top:358px" viewBox="-30 -30 60 60" aria-label="Uniform">
    <circle r="30" fill="var(--uniform)"/>
    <path d="M-7 -12 L-18 -7 L-20 2 L-13 4 L-12 14 L12 14 L13 4 L20 2 L18 -7 L7 -12 L0 -6 Z" fill="none" stroke="var(--white)" stroke-width="3" stroke-linejoin="round"/>
    <circle cx="4" cy="-1" r="2" fill="var(--white)"/>
  </svg>

  <svg class="category-icon" style="top:437px" viewBox="-30 -30 60 60" aria-label="Food day">
    <circle r="30" fill="var(--food)"/>
    <path d="M-15 0 A7 7 0 0 1 -9 -11 A9 9 0 0 1 7 -13 A8 8 0 0 1 15 -2 A5 5 0 0 1 12 4 H-12 A5 5 0 0 1 -15 0 Z" fill="var(--white)"/>
    <path d="M-12 5 H12 L9 17 H-9 Z" fill="var(--white)"/>
    <g stroke="var(--food)" stroke-width="1.5"><line x1="-4" y1="8" x2="-3" y2="14"/><line x1="0" y1="8" x2="0" y2="14"/><line x1="4" y1="8" x2="3" y2="14"/></g>
  </svg>

  <svg class="category-icon" style="top:516px" viewBox="-30 -30 60 60" aria-label="Events">
    <circle r="30" fill="var(--events)"/>
    <rect x="-15" y="-13" width="30" height="29" rx="2" fill="none" stroke="var(--white)" stroke-width="3.5"/>
    <rect x="-15" y="-13" width="30" height="6" fill="var(--white)"/>
    <rect x="-10" y="-18" width="3" height="7" fill="var(--white)"/>
    <rect x="7" y="-18" width="3" height="7" fill="var(--white)"/>
    <path d="M0 -3 L2.4 2.2 L8 2.7 L3.8 6.4 L5 12 L0 9 L-5 12 L-3.8 6.4 L-8 2.7 L-2.4 2.2 Z" fill="var(--white)"/>
  </svg>

  <svg class="category-icon" style="top:593px" viewBox="-30 -30 60 60" aria-label="School camps">
    <circle r="30" fill="var(--camps)"/>
    <path d="M-4 -12 L8 -12 L22 11 L8 11 Z" fill="var(--white)"/>
    <path d="M-6 -10 L4 11 H-10 Z" fill="var(--white)"/>
    <path d="M-10 -1 L-20 14 M-14 5 L-9 14" stroke="var(--white)" stroke-width="2.5" stroke-linecap="round"/>
  </svg>

  <svg class="category-icon" style="top:673px" viewBox="-30 -30 60 60" aria-label="Tuition">
    <circle r="30" fill="var(--tuition)"/>
    <path d="M1 20 L-2 -14 Q0 -22 4 -17 Q6 -10 -6 0 Q-11 6 -6 11 Q0 14 5 8 Q6 2 0 1 Q-5 2 -3 7" fill="none" stroke="var(--white)" stroke-width="2.5" stroke-linecap="round"/>
    <circle cx="-2" cy="19" r="2.5" fill="var(--white)"/>
  </svg>

  <div class="category-label" style="top:252px">Bramble Ridge School<span class="shop-link">School Donation</span></div>
  <div class="category-label" style="top:321px">Bramble Ridge School<span class="shop-link">Trips and Activities</span></div>
  <div class="category-label" style="top:390px">Bramble Ridge School<span class="shop-link">Uniform</span></div>
  <div class="category-label" style="top:459px">Bramble Ridge School<span class="shop-link">Food Day</span></div>
  <div class="category-label" style="top:528px">Bramble Ridge School<span class="shop-link">Events</span></div>
  <div class="category-label" style="top:597px">Bramble Ridge School<span class="shop-link">School Camps</span></div>
  <div class="tuition-label">Tuition</div>

</main>
</body>
</html>
```